" A empresa está localizada numa cidade pequena, porém muito próximos da capital do estado de Minas Gerais e de outras cidades maiores do interior. Considerada região metropolitana da capital. Criaremos um site e faremos venda de produtos na loja virtual, bem como marcação de serviços. Queremos trazer profissionalismo e um serviço diferenciado para a região. Nossa meta é em 3 anos ser a principal referência nesse serviço num raio de 50 km da cidade. "

```html
<!DOCTYPE html>
<html lang="pt-BR">
<head>
<meta charset="UTF-8">
<title>Folha Clara — Tag</title>
<link rel="stylesheet" href="https://fonts.googleapis.com/css2?family=Cinzel:wght@400;500&family=Montserrat:wght@500&display=swap">
<style>
  :root {
    --bg: #e9eaea;
    --tag-dark: #173b3e;
    --tag-mid: #21504f;
    --gold: #c9a55a;
    --mark-faint: rgba(10, 35, 38, 0.35);
  }
  * { margin: 0; padding: 0; box-sizing: border-box; }
  html, body { width: 1200px; height: 1200px; overflow: hidden; background: var(--bg); }
  .canvas { position: relative; width: 1200px; height: 1200px; }
  .tag {
    position: absolute;
    left: 390px;
    top: 110px;
    width: 420px;
    height: 1000px;
  }
  .tag-shape { position: absolute; inset: 0; width: 100%; height: 100%; }
  .tag-content {
    position: absolute;
    left: 0;
    right: 0;
    top: 250px;
    display: flex;
    flex-direction: column;
    align-items: center;
    text-align: center;
    color: var(--gold);
  }
  .brand-dot {
    width: 120px;
    height: 120px;
    border-radius: 50%;
    background: var(--gold);
    margin-bottom: 28px;
  }
  .brand-name {
    font-family: "Cinzel", serif;
    font-weight: 400;
    font-size: 44px;
    letter-spacing: 1px;
    line-height: 1;
    white-space: nowrap;
  }
  .brand-tagline {
    font-family: "Cinzel", serif;
    font-weight: 400;
    font-size: 17px;
    letter-spacing: 1px;
    margin-top: 8px;
  }
  .contact-phone {
    display: flex;
    align-items: center;
    gap: 10px;
    margin-top: 36px;
    font-family: "Montserrat", sans-serif;
    font-weight: 500;
    font-size: 22px;
    color: #f2f2f2;
  }
  .phone-icon { width: 26px; height: 26px; }
  .brand-watermark {
    position: absolute;
    left: 10px;
    right: 10px;
    top: 580px;
    height: 340px;
    border-radius: 50%;
    background: radial-gradient(ellipse at center, var(--mark-faint) 0%, rgba(10, 35, 38, 0.12) 60%, rgba(10, 35, 38, 0) 75%);
  }
</style>
</head>
<body>
<main class="canvas">
  <div class="tag">
    <svg class="tag-shape" viewBox="0 0 420 1000" aria-hidden="true">
      <defs>
        <linearGradient id="tagFill" x1="0" y1="0" x2="1" y2="1">
          <stop offset="0" stop-color="#21504f"/>
          <stop offset="1" stop-color="#173b3e"/>
        </linearGradient>
      </defs>
      <path d="M190 12 Q210 -4 230 12 L408 178 Q420 190 420 206 L420 960 Q420 1000 380 1000 L40 1000 Q0 1000 0 960 L0 206 Q0 190 12 178 Z" fill="url(#tagFill)"/>
      <circle cx="210" cy="80" r="22" fill="#e9eaea"/>
    </svg>
    <div class="brand-watermark" role="img" aria-label="Faint large brand symbol decoration"></div>
    <div class="tag-content">
      <div class="brand-dot" aria-hidden="true"></div>
      <div class="brand-name">FOLHA CLARA</div>
      <div class="brand-tagline">PORQUE VOCÊ É ÚNICA</div>
      <div class="contact-phone">
        <svg class="phone-icon" viewBox="0 0 24 24" aria-hidden="true">
          <circle cx="12" cy="12" r="12" fill="#c9a55a"/>
          <path d="M8.6 6.2c.4-.2.9 0 1.1.4l1 2c.2.4.1.8-.2 1.1l-.8.7c.6 1.3 1.6 2.3 2.9 2.9l.7-.8c.3-.3.7-.4 1.1-.2l2 1c.4.2.6.7.4 1.1l-.5 1.2c-.3.6-.9 1-1.6.9-4-.5-7.1-3.6-7.6-7.6-.1-.7.3-1.3.9-1.6z" fill="#173b3e"/>
        </svg>
        <span>(31) 9 0000-1234</span>
      </div>
    </div>
  </div>
</main>
</body>
</html>
```